New flyer design for construction company marketing and description of services.

I want to have a flyer design that my techs will carry to deliver after job completion or for marketing purposes, to explain what services we provide, we offer General construction services.

Brightnail Handyman Sevices originated from a family-owned and operated contractor business, performing home renovation, addition, and construction work in the NYC area since 2004.

Today, we specialize in reliable and affordable Construction services for residential and commercial clients In 2014, we expanded to northern New Jersey. In 2016, we brought quality home improvement and repair services to new Bucks County, PA, and nearby New Jersey areas.
We offer carpentry, electrical, plumbing, renovation, remodel, cleaning services and landscaping.
I would like to have a section for home rental maintenance.

Target Market(s)

Homeowners, rental properties, real state and Senior citizen

Industry/Entity Type

Construction Company

Colors

Designer to choose colors to be used in the design.

Requirements
Must have
• A special design that will attract 55 + clients maybe a logo version that will be more attractive to seniors. I would updated the briefing with design and previous pictures, but we have all available in our social media instagram and facebook:
• https://www.sampleinsta.test/brightnailhandyman/?hl=en
• https://www.samplefacebook.test/brightnailhandy/
Nice to have
• New design ideas and layouts.

```html
<!DOCTYPE html>
<html lang="en">
<head>
<meta charset="utf-8">
<title>Brightnail Handyman Sevices – Flyer</title>
<link rel="stylesheet" href="https://fonts.googleapis.com/css2?family=Jost:wght@400;500;600;700&display=swap">
<style>
  :root {
    --red: #e2202a;
    --red-dark: #b5161d;
    --yellow: #fdd431;
    --black: #111111;
    --charcoal: #5b5b5d;
    --mid-gray: #8c8c8c;
    --light: #f1f1f1;
    --white: #ffffff;
  }
  * { margin: 0; padding: 0; box-sizing: border-box; }
  html, body { width: 960px; height: 1200px; overflow: hidden; }
  body {
    background: var(--mid-gray);
    font-family: "Jost", "Century Gothic", sans-serif;
    position: relative;
  }
  .flyer {
    position: absolute;
    top: 290px;
    width: 456px;
    height: 642px;
    transform: scale(0.9649);
    transform-origin: 0 0;
    overflow: hidden;
    background: var(--white);
    box-shadow: 0 6px 22px rgba(0,0,0,.35);
  }
  .flyer--front { left: 30px; }
  .flyer--back { left: 490px; }
  .layer { position: absolute; inset: 0; width: 456px; height: 642px; }
  .photo { position: absolute; }

  /* brand mark */
  .brand {
    position: absolute;
    display: flex;
    align-items: center;
    gap: 8px;
  }
  .brand__dot { width: 26px; height: 26px; border-radius: 50%; background: var(--red); }
  .brand__name { font-weight: 700; font-size: 32px; color: var(--red); letter-spacing: -.5px; line-height: 1; }

  /* front */
  .front__photo-top {
    left: 0; top: 0; width: 456px; height: 480px;
    background: linear-gradient(120deg, #e8e8e6 0%, #cfd2d4 35%, #9aa1a8 55%, #f2b430 70%, #6b7280 85%, #2b3240 100%);
  }
  .front__logo-panel { position: absolute; left: 0; top: 0; width: 240px; height: 64px; background: rgba(255,255,255,.85); }
  .front__photo-van {
    left: 0; top: 488px; width: 240px; height: 150px;
    background: linear-gradient(160deg, #b9bcc0 0%, #e7e8ea 35%, #1d1d1f 60%, #6c6f73 100%);
  }
  .about { position: absolute; left: 25px; top: 300px; width: 240px; color: var(--white); }
  .about__title { font-weight: 600; font-size: 13.5px; margin-bottom: 2px; }
  .about__text { font-size: 10.4px; line-height: 13px; text-align: justify; margin-bottom: 14px; }

  .contact-hex {
    position: absolute; left: 243px; top: 458px; width: 213px;
    text-align: center; color: var(--black);
  }
  .contact-hex__title { font-size: 13px; font-weight: 500; display: inline-block; padding-bottom: 2px; border-bottom: 1.5px solid var(--black); margin-bottom: 10px; }
  .contact-hex__item { font-size: 10px; margin-bottom: 8px; }
  .contact-hex__item svg { display: block; margin: 0 auto 4px; }
  .socials { display: flex; gap: 10px; justify-content: center; }
  .socials span { width: 11px; height: 11px; border-radius: 50%; border: 1px solid currentColor; }

  /* back */
  .back__photo-deck {
    left: 0; top: 0; width: 456px; height: 280px;
    background: linear-gradient(180deg, #d9dcdc 0%, #a7aeb0 30%, #4b4f4f 55%, #6b5a4b 80%, #5a4638 100%);
  }
  .back__logo-panel { position: absolute; left: 10px; top: 0; width: 218px; height: 84px; background: rgba(255,255,255,.92); }
  .offer-tab {
    position: absolute; left: 0; top: 292px; width: 136px; height: 26px;
    background: var(--red); color: var(--white);
    font-size: 14px; font-weight: 500; padding: 3px 0 0 46px;
    clip-path: polygon(0 0, 100% 0, 90% 100%, 0 100%);
  }
  .service {
    position: absolute; width: 173px; height: 86px;
    background: var(--charcoal); color: var(--white);
    padding: 24px 0 0 36px;
  }
  .service__title { font-size: 10.5px; font-weight: 500; text-align: center; margin: 0 0 6px -36px; }
  .service__list { list-style: none; font-size: 7px; line-height: 11px; }
  .service__list li::before { content: "\2713"; margin-right: 5px; font-size: 7px; }
  .service--one { left: 33px; top: 350px; }
  .service--two { left: 250px; top: 350px; }
  .service--three { left: 33px; top: 467px; }
  .service--four { left: 250px; top: 467px; }

  .back__contact { position: absolute; left: 40px; top: 595px; color: var(--black); }
  .back__contact-title { font-size: 13px; font-weight: 500; display: inline-block; border-bottom: 1.5px solid var(--black); padding-bottom: 1px; margin-bottom: 5px; }
  .back__contact-line { font-size: 10.5px; display: flex; align-items: center; gap: 6px; margin-left: -8px; }
  .back__links { position: absolute; left: 172px; top: 599px; color: var(--white); font-size: 10px; }
  .back__links div { display: flex; align-items: center; gap: 8px; margin-bottom: 9px; }
  .back__socials { position: absolute; left: 360px; top: 612px; color: var(--white); }
</style>
</head>
<body>

<!-- Front side -->
<section class="flyer flyer--front">
  <div class="photo front__photo-top" role="img" aria-label="Photo of a handyman holding a hammer and yellow hard hat, with a tool belt, in front of a house"></div>
  <div class="front__logo-panel"></div>

  <svg class="layer" viewBox="0 0 456 642" aria-hidden="true">
    <polygon points="0,50 185,94 185,114 0,72" fill="var(--yellow)"/>
    <polygon points="0,78 330,225 330,256 0,106" fill="var(--red)"/>
    <polygon points="0,106 330,256 330,300 285,300 285,480 0,480" fill="var(--white)"/>
    <polygon points="0,112 140,176 140,184 0,122" fill="#7c7c7c"/>
    <polygon points="0,195 80,245 0,292" fill="var(--black)"/>
    <polygon points="0,300 92,246 62,168 285,268 285,480 0,480" fill="var(--red)"/>
    <polygon points="285,268 456,330 456,400 285,472" fill="var(--white)"/>
    <polygon points="303,325 370,378 303,432" fill="var(--charcoal)"/>
    <polygon points="285,472 456,398 456,426 310,490 285,490" fill="var(--black)"/>
    <polygon points="243,470 345,432 456,470 456,642 345,642 243,610" fill="var(--yellow)"/>
    <rect x="0" y="636" width="456" height="6" fill="var(--red)"/>
  </svg>

  <div class="photo front__photo-van" role="img" aria-label="Photo of the company's black branded service van parked on a street"></div>

  <div class="brand" style="left:50px; top:16px;">
    <span class="brand__dot"></span>
    <span class="brand__name">Brightnail</span>
  </div>

  <div class="about">
    <h1 class="about__title">Brightnail Handyman Sevices</h1>
    <p class="about__text">originated from a family-owned and operated contractor business, performing home renovation, addition, and construction work in the NYC area since 2004.</p>
    <p class="about__text">Today, we specialize in reliable and affordable Construction services for residential and commercial clients In 2014, we expanded to northern New Jersey. In 2016, we brought quality home improvement and repair services to new Bucks County, PA, and nearby New Jersey areas.</p>
  </div>

  <div class="contact-hex">
    <h2 class="contact-hex__title">Contact us</h2>
    <div class="contact-hex__item">
      <svg width="10" height="10" viewBox="0 0 10 10"><circle cx="5" cy="5" r="4.4" fill="none" stroke="#111" stroke-width=".9"/><path d="M3.4 2.8 L4.3 2.8 L4.6 4 L4 4.4 Q4.5 5.6 5.6 6 L6 5.4 L7.2 5.7 L7.2 6.6 Q4 6.8 3.4 2.8Z" fill="#111"/></svg>
      (555) 010-2468
    </div>
    <div class="contact-hex__item">
      <svg width="11" height="8" viewBox="0 0 11 8"><rect x=".5" y=".5" width="10" height="7" fill="none" stroke="#111"/><path d="M.5 .5 L5.5 4.5 L10.5 .5" fill="none" stroke="#111"/></svg>
      brightnailhandymannyc@mailbox.test
    </div>
    <div class="contact-hex__item">
      <svg width="10" height="10" viewBox="0 0 10 10"><circle cx="5" cy="5" r="4.4" fill="none" stroke="#111" stroke-width=".9"/><ellipse cx="5" cy="5" rx="2" ry="4.4" fill="none" stroke="#111" stroke-width=".8"/><line x1=".6" y1="5" x2="9.4" y2="5" stroke="#111" stroke-width=".8"/></svg>
      www.brightnail.test
    </div>
    <div class="socials" aria-label="Social media"><span></span><span></span><span></span><span></span></div>
  </div>
</section>

<!-- Back side -->
<section class="flyer flyer--back">
  <div class="photo back__photo-deck" role="img" aria-label="Photo of a finished rooftop deck with curved outdoor sofa and round fire table beside a brick wall"></div>
  <div class="back__logo-panel"></div>
  <div class="brand" style="left:52px; top:24px;">
    <span class="brand__dot"></span>
    <span class="brand__name">Brightnail</span>
  </div>

  <svg class="layer" viewBox="0 0 456 642" aria-hidden="true" style="z-index:0">
    <rect x="0" y="280" width="456" height="362" fill="var(--light)"/>
    <polygon points="0,280 140,280 60,420" fill="#e6e6e6"/>
    <polygon points="140,280 300,280 220,400" fill="#fafafa"/>
    <polygon points="300,280 456,280 456,380" fill="#e4e4e4"/>
    <polygon points="60,420 220,400 130,560" fill="#f8f8f8"/>
    <polygon points="220,400 456,380 340,560" fill="#e9e9e9"/>
    <polygon points="0,420 60,420 0,560" fill="#f6f6f6"/>
    <rect x="0" y="586" width="456" height="56" fill="var(--red)"/>
    <polygon points="0,610 30,586 156,586 156,642 0,642" fill="var(--yellow)"/>
    <polygon points="0,600 34,576 40,580 0,610" fill="var(--black)"/>
  </svg>

  <div class="offer-tab">We Offer :</div>

  <article class="service service--one">
    <h3 class="service__title">General contractor</h3>
    <ul class="service__list"><li>Lorem ipsum dolor sit amet</li><li>Lorem ipsum dolor sit amet</li><li>Lorem ipsum dolor sit amet</li></ul>
  </article>
  <article class="service service--two">
    <h3 class="service__title">Property maintenance</h3>
    <ul class="service__list"><li>Lorem ipsum dolor sit amet</li><li>Lorem ipsum dolor sit amet</li><li>Lorem ipsum dolor sit amet</li></ul>
  </article>
  <article class="service service--three">
    <h3 class="service__title">Cleaning services</h3>
    <ul class="service__list"><li>Lorem ipsum dolor sit amet</li><li>Lorem ipsum dolor sit amet</li><li>Lorem ipsum dolor sit amet</li></ul>
  </article>
  <article class="service service--four">
    <h3 class="service__title">Handyman services</h3>
    <ul class="service__list"><li>Lorem ipsum dolor sit amet</li><li>Lorem ipsum dolor sit amet</li><li>Lorem ipsum dolor sit amet</li></ul>
  </article>

  <svg class="layer" viewBox="0 0 456 642" aria-hidden="true" style="pointer-events:none">
    <g fill="var(--red)">
      <polygon points="119,309 138,320 138,342 119,353 100,342 100,320"/>
      <polygon points="336,309 355,320 355,342 336,353 317,342 317,320"/>
      <polygon points="119,426 138,437 138,459 119,470 100,459 100,437"/>
      <polygon points="336,426 355,437 355,459 336,470 317,459 317,437"/>
    </g>
    <g fill="none" stroke="var(--yellow)" stroke-width="1.6">
      <circle cx="119" cy="331" r="6"/>
      <path d="M330 336 L336 325 L342 336 Z"/>
      <line x1="114" y1="455" x2="124" y2="440"/>
      <circle cx="336" cy="448" r="6"/>
    </g>
  </svg>

  <div class="back__contact">
    <h2 class="back__contact-title">Contact us</h2>
    <div class="back__contact-line">
      <svg width="10" height="10" viewBox="0 0 10 10"><circle cx="5" cy="5" r="4.4" fill="none" stroke="#111" stroke-width=".9"/><path d="M3.4 2.8 L4.3 2.8 L4.6 4 L4 4.4 Q4.5 5.6 5.6 6 L6 5.4 L7.2 5.7 L7.2 6.6 Q4 6.8 3.4 2.8Z" fill="#111"/></svg>
      (555) 010-2468
    </div>
  </div>

  <div class="back__links">
    <div>
      <svg width="11" height="8" viewBox="0 0 11 8"><rect x=".5" y=".5" width="10" height="7" fill="none" stroke="#fff"/><path d="M.5 .5 L5.5 4.5 L10.5 .5" fill="none" stroke="#fff"/></svg>
      brightnailhandymannyc@mailbox.test
    </div>
    <div>
      <svg width="10" height="10" viewBox="0 0 10 10"><circle cx="5" cy="5" r="4.4" fill="none" stroke="#fff" stroke-width=".9"/><ellipse cx="5" cy="5" rx="2" ry="4.4" fill="none" stroke="#fff" stroke-width=".8"/><line x1=".6" y1="5" x2="9.4" y2="5" stroke="#fff" stroke-width=".8"/></svg>
      www.brightnail.test
    </div>
  </div>
  <div class="socials back__socials" aria-label="Social media"><span></span><span></span><span></span><span></span></div>
</section>

</body>
</html>
```